Salon and Spa Distributor Business Card

Need a business card. We are are distributor in the salon and spa industry. We identify with natural beauty. Need a card with:
Company Name: Petal Haven"
Title: "President & CEO"
Address
Company Phone number
email
website
Tag Line:" The Professional Salon Source"

Industry/Entity Type

Business

Contact Information for Business Card

Name: Lena Morcott
Title: "President & CEO"
Address: 317 Birchfield Ln, Oakvane, NJ 07481
Company Phone number: 800-463-9152
email: lenamorcott@petalhaven-example.com
website: www.petalhaven-example.com

Requirements
Should not have
• No black backgrounds

```html
<!DOCTYPE html>
<html lang="en">
<head>
<meta charset="utf-8">
<title>Petal Haven Business Card</title>
<link rel="stylesheet" href="https://fonts.googleapis.com/css2?family=Questrial&family=Open+Sans:wght@400;600;700&display=swap">
<style>
  :root {
    --canvas: #ecebe7;
    --card-front: #f2f7ef;
    --card-light: #ffffff;
    --green: #3fae3f;
    --green-soft: #8fd28a;
    --green-deep: #1f8a2e;
    --grey-text: #555555;
    --grey-strong: #333333;
    --grey-muted: #7a7a7a;
    --line: #e4e4e4;
    --shadow: rgba(0,0,0,0.18);
  }
  * { box-sizing: border-box; margin: 0; padding: 0; }
  html, body { width: 1200px; height: 800px; overflow: hidden; }
  body {
    background: var(--canvas);
    position: relative;
    font-family: "Open Sans", sans-serif;
  }
  .card {
    position: absolute;
    top: 245px;
    width: 540px;
    height: 310px;
    border-radius: 16px;
    box-shadow: 0 10px 28px var(--shadow);
    overflow: hidden;
  }
  .card-front { left: 40px; background: var(--card-front); }
  .card-back { left: 620px; background: var(--card-light); }

  /* front */
  .front-brand {
    position: absolute;
    left: 0; right: 0; top: 112px;
    display: flex; flex-direction: column; align-items: center;
  }
  .brand-line { display: flex; align-items: center; gap: 14px; }
  .brand-dot {
    width: 26px; height: 26px; border-radius: 50%;
    background: var(--green);
  }
  .brand-name {
    font-family: "Questrial", sans-serif;
    color: var(--green);
    font-size: 46px;
    letter-spacing: 0.5px;
    line-height: 1;
  }
  .tagline {
    margin-top: 10px;
    margin-left: 40px;
    font-family: "Questrial", sans-serif;
    color: var(--grey-muted);
    font-size: 15px;
    letter-spacing: 1px;
  }

  /* back */
  .back-art {
    position: absolute;
    left: 0; top: 0; bottom: 0;
    width: 220px;
    background: linear-gradient(135deg, #e9f6e7 0%, var(--green-soft) 55%, var(--green) 100%);
  }
  .back-info {
    position: absolute;
    left: 248px; top: 30px; right: 20px;
  }
  .back-brand { display: flex; align-items: center; gap: 8px; }
  .back-brand .brand-dot { width: 14px; height: 14px; }
  .back-brand .brand-name { font-size: 24px; }
  .divider {
    height: 1px; background: var(--line);
    margin: 14px 0 20px;
  }
  .person-name {
    font-size: 21px; color: var(--grey-text); line-height: 1.1;
  }
  .person-name strong { font-weight: 700; color: var(--grey-strong); }
  .person-title {
    font-size: 14px; font-weight: 600; color: var(--green);
    margin-top: 3px;
  }
  .contact-list { list-style: none; margin-top: 16px; }
  .contact-list li {
    display: flex; align-items: center; gap: 9px;
    font-size: 11.5px; color: var(--grey-text);
    margin-bottom: 7px;
    white-space: nowrap;
  }
  .contact-list svg { width: 13px; height: 13px; flex: none; fill: var(--green); }
</style>
</head>
<body>

<section class="card card-front">
  <div class="front-brand">
    <div class="brand-line">
      <span class="brand-dot"></span>
      <span class="brand-name">Petal Haven</span>
    </div>
    <p class="tagline">The Professional Salon Source</p>
  </div>
</section>

<section class="card card-back">
  <div class="back-art" role="img" aria-label="Large green brand illustration area"></div>
  <div class="back-info">
    <div class="back-brand">
      <span class="brand-dot"></span>
      <span class="brand-name">Petal Haven</span>
    </div>
    <div class="divider"></div>
    <p class="person-name">Lena <strong>Morcott</strong></p>
    <p class="person-title">President &amp; CEO</p>
    <ul class="contact-list">
      <li>
        <svg viewBox="0 0 16 16"><path d="M8 0a5.5 5.5 0 0 0-5.5 5.5C2.5 10 8 16 8 16s5.5-6 5.5-10.5A5.5 5.5 0 0 0 8 0zm0 7.8a2.3 2.3 0 1 1 0-4.6 2.3 2.3 0 0 1 0 4.6z"/></svg>
        317 Birchfield Ln, Oakvane, NJ 07481
      </li>
      <li>
        <svg viewBox="0 0 16 16"><path d="M1 4c0-1.5 3-3 7-3s7 1.5 7 3v1.5h-3.5V4h-7v1.5H1z"/><rect x="2.5" y="7" width="11" height="8" rx="1.5"/></svg>
        800-463-9152
      </li>
      <li>
        <svg viewBox="0 0 16 16"><path d="M0 3h16v1.2L8 9 0 4.2z"/><path d="M0 5.8 8 10.6l8-4.8V13H0z"/></svg>
        lenamorcott@petalhaven-example.com
      </li>
      <li>
        <svg viewBox="0 0 16 16"><path d="M8 0a8 8 0 1 0 0 16A8 8 0 0 0 8 0zm5.9 7.3h-2.6a12 12 0 0 0-1-5 6.3 6.3 0 0 1 3.6 5zM8 1.6c.8 1 1.6 3 1.7 5.7H6.3C6.4 4.6 7.2 2.6 8 1.6zM5.7 2.3a12 12 0 0 0-1 5H2.1a6.3 6.3 0 0 1 3.6-5zM2.1 8.7h2.6a12 12 0 0 0 1 5 6.3 6.3 0 0 1-3.6-5zM8 14.4c-.8-1-1.6-3-1.7-5.7h3.4c-.1 2.7-.9 4.7-1.7 5.7zm2.3-.7a12 12 0 0 0 1-5h2.6a6.3 6.3 0 0 1-3.6 5z"/></svg>
        www.petalhaven-example.com
      </li>
    </ul>
  </div>
</section>

</body>
</html>
```